Los Fogones Ember Poultry MENU!

We are looking for a simple, rustic and modern menu that highlights our passion for healthy and tasty chickens!
We want to highlight our menu but yet keep it very simple.

Attached is info on our logo and our menu information

Target Market(s)

We want to attract all customers but primarily we want to focus on the following 3 markets: Healthy concerned, Food fanatics and Family based.

Industry/Entity Type

Fast Food Restaurant

Requirements
Must have
• We must have our logo on the flyer,
• rustic yet modern
• you must use our colors on the flyer and
• KEEP IT SIMPLE
• Here is our Menu below
• Attached is our final menu we are going to advertise:
• Chicken:
• 1/4 Chicken Dark $6.99
• 1/4 Chicken White $7.99
• 1/2 Chicken white + dark $9.99
• 1/2 chicken all white $10.99
• All come with choice of 2 small sides
• 1 whole chicken family meal ( served with 3 Large sides + 2 liter soda) $23.99
• 2 whole chicken family meal (served with 4 Large sides + 2 liter soda) $33.99
• Extra whole chicken (Chicken only) $13.99
• Sides available with meals:
• - Cilantro infused white rice
• - Hand Cut Fries
• - Hand Cut Sweet potato Fries
• - Yucca
• - Fried Plantains
• - Pinto Beans
• - Black Beans
• - Steamed vegetable medley
• - Cesar Salad
• - Garden Salad
• - House Salad
• - Tortillas
• (reg side: $1.99) Large Side $3.29
• Other Dishes available:
• Lomo Saltado: $12.99
• Pesto Pasta (Tallarin Verde) w/ Steak or 1/4 chicken $ 12.99
• Bistek a lo Pobre: $12.99
• Marcos Treat $12.99 (Chicken filet grilled) w/ salads
• Tallarin Saltado (Garden style pasta) w/ Chicken $11.99, Steak add. $1.49
• Tallarin a la Huancaina $12.99 w/ steak or 1/4 chicken
• Garden Salad ($6.99) Add chicken or steak $1.99
• Cesar Salad ($6.99) Add Chicken or steak $1.99
• House Salad ($6.99) Add chicken or steak $1.99
• DRINKS/DESSERTS:
• - SODAS: REG. $1.99 LARGE 2.59
• - ANDA FIZZ: $1.69 CAN; $1.99 IMPORTED; $2.59 BOTTLE
• - SPECIALTY DRINKS: $2.59
• - ALFAJOR $2.99
• - PERUVIAN FLAN $4.99
• - 3 LECHES $4.99
• (SAVE $1.00 OF ANY DESSERT WITH PURCHASE OF MEAL)
Nice to have
• We would love to see it all in 1 half sheet
Should not have
• can not have too much on it where its confusing.

```html
<!DOCTYPE html>
<html lang="en">
<head>
<meta charset="utf-8">
<title>Los Fogones Ember Poultry — Menu</title>
<link href="https://fonts.googleapis.com/css2?family=Roboto+Slab:wght@700;900&family=Open+Sans:wght@400;600;700&display=swap" rel="stylesheet">
<style>
:root{
  --page:#e9e9ea;
  --paper-light:#efe4d6;
  --paper-mid:#d8c4ad;
  --stripe:rgba(120,84,56,.10);
  --red:#c4161c;
  --brown:#5a3a26;
  --ink:#3b2a1f;
  --flame:#e8731c;
  --shadow:rgba(0,0,0,.28);
}
*{box-sizing:border-box;margin:0;padding:0}
html,body{width:849px;height:1200px;overflow:hidden}
body{background:var(--page);font-family:"Open Sans",sans-serif;color:var(--ink);
  display:flex;flex-direction:column;align-items:center;justify-content:space-between;padding:60px 0}
.spread{width:760px;height:500px;display:flex;box-shadow:0 12px 28px var(--shadow)}
.panel{position:relative;width:50%;height:100%;overflow:hidden;
  background:
    repeating-linear-gradient(90deg,var(--stripe) 0 3px,transparent 3px 9px),
    radial-gradient(ellipse at 50% 40%,var(--paper-light) 0%,var(--paper-mid) 100%)}
.panel + .panel{border-left:1px solid rgba(90,58,38,.25)}
.photo{position:absolute;left:0;right:0}
.photo-chicken{background:linear-gradient(135deg,#7a2d0f,#c4561c 45%,#e59a3a 70%,#8a3a14)}
.photo-plate{background:radial-gradient(ellipse at 50% 55%,#d88a3a 0%,#a8481a 40%,#4f7a2a 70%,#e9ddcc 100%)}
.photo-salad{background:radial-gradient(ellipse at 45% 50%,#e8d8a8 0%,#7fa24a 35%,#c2342a 55%,#f1ece2 80%)}
.brand{display:flex;align-items:center;justify-content:center;gap:7px;
  font-family:"Roboto Slab",serif;font-weight:900;color:var(--red);letter-spacing:.5px}
.brand .dot{width:12px;height:12px;border-radius:50%;background:var(--flame)}
/* back cover */
.back .photo-chicken{top:0;height:170px}
.back .brand{margin-top:215px;font-size:19px}
.back .contact{text-align:center;margin-top:30px;font-size:9px;line-height:1.6;color:var(--brown)}
.contact .line{display:flex;align-items:center;justify-content:center;gap:5px}
.contact svg{width:10px;height:10px;fill:var(--brown)}
.back .phone{margin-top:6px;font-family:"Roboto Slab",serif;font-weight:700;font-size:18px;color:var(--red)}
/* front cover */
.front .brand{margin-top:34px;font-size:19px}
.front .title{text-align:center;margin-top:40px;font-family:"Roboto Slab",serif;font-weight:900;
  font-size:62px;color:var(--red);letter-spacing:2px}
.front .photo-plate{left:30px;right:30px;top:210px;bottom:46px;border-radius:6px}
/* inside */
.menu-list{position:absolute;left:26px;right:26px;top:24px}
.section-title{font-family:"Roboto Slab",serif;font-weight:700;color:var(--red);font-size:12px;
  text-transform:uppercase;border-bottom:1px solid var(--red);padding-bottom:2px;margin:8px 0 5px;
  display:flex;justify-content:space-between}
.section-title small{font-family:"Open Sans",sans-serif;font-size:8px;color:var(--brown);align-self:flex-end}
.item{display:flex;justify-content:space-between;font-size:9.5px;line-height:14px}
.item .price{font-weight:700;color:var(--brown)}
.item .price + .price{margin-left:14px}
.note{font-size:8px;font-style:italic;color:var(--brown);margin-top:2px}
.inside-left .photo-chicken{bottom:0;height:120px}
.inside-right .photo-salad{bottom:0;height:190px}
</style>
</head>
<body>

<section class="spread cover">
  <div class="panel back">
    <div class="photo photo-chicken" role="img" aria-label="Close-up of charcoal roasted chicken pieces"></div>
    <div class="brand"><span class="dot"></span>LOS FOGONES</div>
    <div class="contact">
      <p class="line"><svg viewBox="0 0 10 10"><path d="M5 0a3.5 3.5 0 0 0-3.5 3.5C1.5 6 5 10 5 10s3.5-4 3.5-6.5A3.5 3.5 0 0 0 5 0zm0 5a1.5 1.5 0 1 1 0-3 1.5 1.5 0 0 1 0 3z"/></svg>1280 Ember Lane, Fairview, ST 00000</p>
      <p class="phone">555-014-2290</p>
    </div>
  </div>
  <div class="panel front">
    <div class="brand"><span class="dot"></span>LOS FOGONES</div>
    <h1 class="title">MENU</h1>
    <div class="photo photo-plate" role="img" aria-label="Whole roasted chicken on a plate with potatoes and greens"></div>
  </div>
</section>

<section class="spread inside">
  <div class="panel inside-left">
    <div class="menu-list">
      <h2 class="section-title">Chicken</h2>
      <p class="item"><span>1/4 Chicken Dark</span><span class="price">$6.99</span></p>
      <p class="item"><span>1/4 Chicken White</span><span class="price">$7.99</span></p>
      <p class="item"><span>1/2 Chicken White + Dark</span><span class="price">$9.99</span></p>
      <p class="item"><span>1/2 Chicken All White</span><span class="price">$10.99</span></p>
      <p class="note">All come with choice of 2 small sides</p>
      <p class="item"><span>1 Whole Chicken Family Meal</span><span class="price">$23.99</span></p>
      <p class="item"><span>2 Whole Chicken Family Meal</span><span class="price">$33.99</span></p>
      <p class="item"><span>Extra Whole Chicken</span><span class="price">$13.99</span></p>
      <h2 class="section-title">Sides available with meals <small>Reg &nbsp; Large</small></h2>
      <p class="item"><span>Cilantro White Rice</span><span><span class="price">$1.99</span><span class="price">$3.29</span></span></p>
      <p class="item"><span>Hand Cut Fries</span><span><span class="price">$1.99</span><span class="price">$3.29</span></span></p>
      <p class="item"><span>Sweet Potato Fries</span><span><span class="price">$1.99</span><span class="price">$3.29</span></span></p>
      <p class="item"><span>Yucca</span><span><span class="price">$1.99</span><span class="price">$3.29</span></span></p>
      <p class="item"><span>Fried Plantains</span><span><span class="price">$1.99</span><span class="price">$3.29</span></span></p>
      <p class="item"><span>Pinto or Black Beans</span><span><span class="price">$1.99</span><span class="price">$3.29</span></span></p>
    </div>
    <div class="photo photo-chicken" role="img" aria-label="Row of grilled chicken pieces"></div>
  </div>
  <div class="panel inside-right">
    <div class="menu-list">
      <h2 class="section-title">Other Dishes</h2>
      <p class="item"><span>Lomo Saltado</span><span class="price">$12.99</span></p>
      <p class="item"><span>Tallarin Verde w/ Steak or 1/4 Chicken</span><span class="price">$12.99</span></p>
      <p class="item"><span>Bistek a lo Pobre</span><span class="price">$12.99</span></p>
      <p class="item"><span>Marcos Treat w/ Salads</span><span class="price">$12.99</span></p>
      <p class="item"><span>Tallarin Saltado w/ Chicken</span><span class="price">$11.99</span></p>
      <p class="item"><span>Tallarin a la Huancaina</span><span class="price">$12.99</span></p>
      <p class="item"><span>Garden, Cesar or House Salad</span><span class="price">$6.99</span></p>
      <h2 class="section-title">Drinks / Desserts</h2>
      <p class="item"><span>Sodas Reg. / Large</span><span class="price">$1.99 / $2.59</span></p>
      <p class="item"><span>Anda Fizz Can</span><span class="price">$1.69</span></p>
      <p class="item"><span>Specialty Drinks</span><span class="price">$2.59</span></p>
      <p class="item"><span>Alfajor</span><span class="price">$2.99</span></p>
      <p class="item"><span>Peruvian Flan / 3 Leches</span><span class="price">$4.99</span></p>
    </div>
    <div class="photo photo-salad" role="img" aria-label="Caesar salad with grilled chicken and tomatoes"></div>
  </div>
</section>

</body>
</html>
```